Tree Pruning Website

We need a website for a tree Arborist, pruning company called Hollow Ridge Branchworks. We look after all types of trees, knock down trees and prune trees. Our target market is from domestic clients to government clients and everything in between.

We would like to see the use of our main colours which are orange and green

We are not looking forward in seeing a template that we have seen before but a unique template. We have designed 5 templates ourselves and we wish for the design community to take our designs to the next level.

We have also designed a template for things that **we are not** looking for (Version 4)

To make it fair for everyone, we are also not giving out any participation payments as we have had. One winner will take all of the payment!!!

I Have attached a image of the designs and a image of a tree.

We are just looking at the PSD file been developed. We have our own team who can slice the image up into a HTML format.

Target Market(s)

Everyone who needs to cut down a tree

Industry/Entity Type

Government

Requirements
Must have
• Logo on front page
A List of our services
jQuery slider on page
Phone Number on every page

```html
<!DOCTYPE html>
<html lang="en">
<head>
<meta charset="utf-8">
<title>Hollow Ridge Branchworks</title>
<link href="https://fonts.googleapis.com/css2?family=Fenix&family=Open+Sans:wght@300;400&display=swap" rel="stylesheet">
<style>
:root{
  --orange:#e8661c;
  --orange-dark:#d65512;
  --orange-text:#f15a0f;
  --green-dark:#1c6a3b;
  --green-icon:#7fa42a;
  --green-foot-top:#b8d47a;
  --green-foot-bot:#6e9a1f;
  --body:#444;
  --nav-top:#fbfbfb;
  --nav-bot:#e4e4e4;
  --card:#f3f3f3;
}
*{box-sizing:border-box;margin:0;padding:0}
html,body{width:1200px;height:1142px;overflow:hidden;background:#fff}
body{position:relative;font-family:"Open Sans",sans-serif;color:var(--body)}
.header{position:absolute;left:0;top:0;width:1200px;height:147px;background:linear-gradient(180deg,var(--orange) 0%,var(--orange-dark) 100%)}
.brand{position:absolute;left:221px;top:36px;display:flex;align-items:center;gap:10px}
.brand-dot{width:30px;height:30px;border-radius:50%;background:#fff}
.brand-name{font-family:"Fenix",serif;font-size:26px;color:#fff;line-height:1}
.phone{position:absolute;right:210px;top:46px;font-family:"Fenix",serif;color:#fff;font-size:14px}
.phone strong{font-size:19px;font-weight:400;letter-spacing:.5px;margin-left:3px}
.hero{position:absolute;left:0;top:147px;width:1200px;height:362px;background:linear-gradient(160deg,#4f7a2c 0%,#8fc04a 35%,#6fa43a 60%,#3d5b2a 100%)}
.hero::after{content:"";position:absolute;left:0;right:0;bottom:0;height:10px;background:linear-gradient(180deg,rgba(0,0,0,0),rgba(0,0,0,.35))}
.hero-title{position:absolute;left:208px;top:125px;width:515px;font-family:"Fenix",serif;font-weight:400;font-size:44px;line-height:34px;color:#fff;text-transform:uppercase;text-shadow:0 2px 3px rgba(0,0,0,.45)}
.nav{position:absolute;left:209px;top:103px;width:783px;height:91px;display:flex;border-radius:4px 4px 0 0;overflow:hidden;box-shadow:0 2px 4px rgba(0,0,0,.25);z-index:2}
.nav-item{flex:1;background:linear-gradient(180deg,var(--nav-top),var(--nav-bot));border-right:1px solid #d2d2d2;border-left:1px solid #fff;display:flex;flex-direction:column;align-items:center;padding-top:17px;font-family:"Fenix",serif;font-size:17px;color:#3b3b3b}
.nav-item:last-child{border-right:none}
.nav-item.is-active{background:linear-gradient(180deg,#ececec,#f8f8f8)}
.nav-icon{width:37px;height:37px;border-radius:50%;background:radial-gradient(circle at 40% 35%,#a9cc4c,var(--green-icon) 60%,#5f8418);box-shadow:0 1px 2px rgba(0,0,0,.3);display:flex;align-items:center;justify-content:center;margin-bottom:5px}
.motto{position:absolute;left:208px;top:537px;width:780px;font-family:"Fenix",serif;font-weight:400;font-size:29px;line-height:34px;color:var(--orange-text)}
.motto b{font-weight:400;color:#111}
.intro{position:absolute;left:208px;top:622px;width:780px;font-size:12.8px;font-weight:300;line-height:19.2px;color:var(--body)}
.divider{position:absolute;left:0;top:754px;width:1200px;height:1px;background:#d6d6d6}
.divider::after{content:"";position:absolute;left:200px;right:200px;top:1px;height:14px;background:radial-gradient(ellipse at 50% 0,rgba(0,0,0,.12),rgba(0,0,0,0) 70%)}
.works-title{position:absolute;left:0;width:1200px;top:768px;text-align:center;font-family:"Fenix",serif;font-weight:400;font-size:29px;color:var(--green-dark)}
.card{position:absolute;top:826px;width:238px;height:187px;background:linear-gradient(180deg,#fafafa,var(--card));box-shadow:0 1px 3px rgba(0,0,0,.25);border-radius:2px;overflow:hidden}
.card-ribbon{position:absolute;left:0;top:0;z-index:1}
.card-art{position:absolute;left:71px;top:14px;width:96px;height:96px;border-radius:10px;background:radial-gradient(circle,#cfcfcf,#ececec 75%)}
.card-text{position:absolute;left:14px;right:14px;top:129px;text-align:center;font-size:11.3px;line-height:16px;color:#3c3c3c}
.footer{position:absolute;left:0;top:1065px;width:1200px;height:77px;border-top:1px solid #8aa64a;background:linear-gradient(180deg,var(--green-foot-top),var(--green-foot-bot))}
.foot-links{position:absolute;left:212px;top:22px;font-size:11.5px;color:#1f2a10}
.foot-links span{margin:0 4px;color:#2f3b1b}
.copyright{position:absolute;left:212px;top:46px;font-size:11px;color:#f4f8ea}
.follow{position:absolute;left:720px;top:30px;font-size:12.6px;color:#1f2a10}
.socials{position:absolute;left:804px;top:18px;display:flex;gap:3px}
.social{width:34px;height:34px;border-radius:50%;background:#fff}
</style>
</head>
<body>
<svg width="0" height="0" style="position:absolute"><defs><linearGradient id="ribbon-fill" x1="0" y1="0" x2="1" y2="1"><stop offset="0" stop-color="#ff6a10"/><stop offset="1" stop-color="#e04e06"/></linearGradient></defs></svg>

<header class="header">
  <div class="brand"><span class="brand-dot"></span><span class="brand-name">Hollow Ridge Branchworks</span></div>
  <div class="phone">Call us at <strong>08 5550 1942</strong></div>
</header>

<nav class="nav">
  <div class="nav-item"><span class="nav-icon"><svg width="18" height="18" viewBox="0 0 18 18"><path d="M9 2 1 9h2.5v7h4v-4h3v4h4V9H17z" fill="#fff"/></svg></span>Home</div>
  <div class="nav-item is-active"><span class="nav-icon"><svg width="18" height="18" viewBox="0 0 18 18"><circle cx="9" cy="7" r="6" fill="#fff"/><rect x="8" y="10" width="2" height="7" fill="#fff"/></svg></span>About us</div>
  <div class="nav-item"><span class="nav-icon"><svg width="20" height="20" viewBox="0 0 20 20"><circle cx="7" cy="12" r="4.5" fill="none" stroke="#fff" stroke-width="3" stroke-dasharray="2.2 1.4"/><circle cx="14" cy="6" r="3" fill="none" stroke="#fff" stroke-width="2.5" stroke-dasharray="1.8 1.2"/></svg></span>Our Services</div>
  <div class="nav-item"><span class="nav-icon"><svg width="20" height="20" viewBox="0 0 20 20"><circle cx="7" cy="12" r="4.5" fill="none" stroke="#fff" stroke-width="3" stroke-dasharray="2.2 1.4"/><circle cx="14" cy="6" r="3" fill="none" stroke="#fff" stroke-width="2.5" stroke-dasharray="1.8 1.2"/></svg></span>Works</div>
  <div class="nav-item"><span class="nav-icon"><svg width="20" height="18" viewBox="0 0 20 18"><path d="M10 1C5 1 1 4.3 1 8.3c0 2.2 1.2 4.1 3.1 5.4L3.5 17l4-2.3c.8.2 1.6.3 2.5.3 5 0 9-3.3 9-7.3S15 1 10 1z" fill="#fff"/></svg></span>Get a Quote</div>
  <div class="nav-item"><span class="nav-icon"><svg width="18" height="18" viewBox="0 0 18 18"><path d="M12.5 2 16 5.5 7 14.5 3 15l.5-4z" fill="#fff"/></svg></span>Contact us</div>
</nav>

<section class="hero" role="img" aria-label="Photograph of a leafy green tree canopy with tall trunks">
  <h1 class="hero-title">We are a leading tree pruning service provider located at Perth.</h1>
</section>

<h2 class="motto">Our motto is when you call, we <b>GUARANTEE</b> to turn up and <b>PROVIDE CARE</b> to our customers.</h2>
<p class="intro">Lorem ipsum dolor sit amet, consectetur adipiscing elit. In ac euismod nisi. Quisque ac diam in est faucibus volutpat ut ac quam. Donec posuere dictum orci ut fringilla. Quisque velit lacus, mattis in placerat eget, consequat et risus. Donec laoreet molestie odio quis mattis. Phasellus vitae turpis posuere turpis interdum varius sed vel eros. Nulla quis dictum diam. Curabitur hendrerit viverra augue, ac consequat nulla tempor ut. Morbi arcu erat, lobortis eu aliquet ac, congue sed libero. Pellentesque sem risus, fringilla in dictum vitae, hendrerit nec risus. Curabitur a venenatis urna.</p>

<div class="divider"></div>
<h2 class="works-title">Our Works</h2>

<article class="card" style="left:215px">
  <div class="card-art" role="img" aria-label="Illustration of a globe"></div>
  <svg class="card-ribbon" width="100" height="92" viewBox="0 0 100 92"><path d="M0 0H96L0 88Z" fill="url(#ribbon-fill)"/><text text-anchor="middle" dominant-baseline="central" transform="translate(38 40) rotate(-45)" font-family="Open Sans,sans-serif" font-size="12.5" fill="#fff">Domestic</text></svg>
  <p class="card-text">Duis pellentesque feugiat mauris, sodales suscipit leo blandit ut. Duis varius convallis pharetra.</p>
</article>

<article class="card" style="left:481px">
  <div class="card-art" role="img" aria-label="Illustration of a business client in a suit"></div>
  <svg class="card-ribbon" width="100" height="92" viewBox="0 0 100 92"><path d="M0 0H96L0 88Z" fill="url(#ribbon-fill)"/><text text-anchor="middle" dominant-baseline="central" transform="translate(38 40) rotate(-45)" font-family="Open Sans,sans-serif" font-size="12.5" fill="#fff">Commercial</text></svg>
  <p class="card-text">Quisque viverra faucibus quam id molestie. Morbi at dui non eros dignissim cursus eget ac enim.</p>
</article>

<article class="card" style="left:746px">
  <div class="card-art" role="img" aria-label="Illustration of a house with an orange roof"></div>
  <svg class="card-ribbon" width="100" height="92" viewBox="0 0 100 92"><path d="M0 0H96L0 88Z" fill="url(#ribbon-fill)"/><text text-anchor="middle" dominant-baseline="central" transform="translate(38 40) rotate(-45)" font-family="Open Sans,sans-serif" font-size="12.5" fill="#fff">Government</text></svg>
  <p class="card-text">Sed consectetur venenatis odio, a sodales lectus laoreet eget. Maecenas quis sem lectus</p>
</article>

<footer class="footer">
  <div class="foot-links">Home<span>/</span>About us<span>/</span>Our Services<span>/</span>Works<span>/</span>Get a Quote<span>/</span>Contact us</div>
  <div class="copyright">Copyright © Ridgeline Studio. All rights reserved</div>
  <div class="follow">Follow us on</div>
  <div class="socials">
    <span class="social" aria-label="Social profile 1"></span>
    <span class="social" aria-label="Social profile 2"></span>
    <span class="social" aria-label="Social profile 3"></span>
    <span class="social" aria-label="Social profile 4"></span>
    <span class="social" aria-label="Social profile 5"></span>
  </div>
</footer>
</body>
</html>
```